Juice up my new website for book profits on Orbimart

I have a website that needs a new look. I made a video of the past and in progress website: http://vexaclip.net/tq8mzR2KWD.... here is the site in progress. http://brew.corestretchguide.net/...this will be a WordPress website......https://pagevault.example/snap/20180305134456/http://www.pressing-tips.net/

This website is setup to primary sell on Orbimart.

eBook: https://www.orbimart.example/Nectar-Blend-Formulas-For-Vigor-ebook/dp/K7RQPWZ2XN/ref=sr_1_4?dchild=1&keywords=Nectar+and+Blend+formulas+for+vigor&qid=1634055930&s=books&sr=1-4

Target Market(s)

Health and weight conscience people

Industry/Entity Type

Health

Number of Pages Required

2 page

Font styles to use
Serif

Requirements
Must have
• slider, sign up form, buy the ebook or hardcopy book.
Nice to have
• happy people drinking juice
Should not have
• Sidebar

```html
<!DOCTYPE html>
<html lang="en">
<head>
<meta charset="utf-8">
<title>Nectar Notes – Juice &amp; Smoothie Recipes</title>
<link href="https://fonts.googleapis.com/css2?family=Playfair+Display:wght@700;900&family=Poppins:wght@400;500;600&display=swap" rel="stylesheet">
<style>
:root{
  --brand-red:#d4372c;
  --ink:#2b2b2b;
  --muted:#7a7a7a;
  --line:#e4e4e4;
  --orange:#f6955c;
  --purple:#4a2f86;
  --lavender:#ece8f8;
  --lavender-deep:#d9d2f1;
  --footer:#7b6cc6;
  --card:#ffffff;
  --star:#f5b417;
}
*{box-sizing:border-box;margin:0;padding:0}
html,body{width:1200px;height:4856px;overflow:hidden;background:#fff}
body{font-family:"Poppins",sans-serif;color:var(--ink);position:relative}
.page{position:relative;width:1200px;height:4856px;overflow:hidden}
.abs{position:absolute}

/* header */
.site-header{left:0;top:0;width:1200px;height:120px;text-align:center}
.brand{margin-top:14px;font-family:"Playfair Display",serif;font-weight:900;font-size:40px;color:var(--brand-red);letter-spacing:1px}
.tagline{font-size:12px;color:var(--brand-red)}
.main-nav{margin:14px auto 0;width:1024px;border-bottom:1px solid var(--line);padding-bottom:10px;display:flex;justify-content:center;gap:34px;font-size:15px;color:#555}

/* hero slider */
.hero{left:88px;top:124px;width:1024px;height:476px;overflow:hidden}
.hero-img{width:100%;height:100%;background:linear-gradient(180deg,#d8dee0 0%,#c7cdd0 38%,#f2a54a 55%,#e6c24f 68%,#e98b3f 82%,#f0f0ec 100%)}
.slider-arrow{top:220px;width:40px;height:40px;display:flex;align-items:center;justify-content:center}
.slider-dots{bottom:18px;left:0;width:100%;display:flex;justify-content:center;gap:10px}
.slider-dots span{width:10px;height:10px;border-radius:50%;background:#fff;opacity:.6}
.slider-dots span.on{opacity:1}
.hero-strip{left:88px;top:600px;width:1024px;height:124px;background:var(--lavender);display:grid;grid-template-columns:1fr 1fr 1fr;padding:24px}
.hero-strip p{font-size:15px;line-height:1.55;color:#444;padding:0 22px}
.hero-strip p+p{border-left:1px solid var(--lavender-deep)}

/* section label pill */
.pill{background:var(--orange);color:#fff;font-size:15px;font-weight:600;letter-spacing:.5px;padding:9px 22px;border-radius:22px;text-transform:uppercase}

/* recipes */
.recipe{width:312px}
.recipe .thumb{height:240px;width:100%}
.recipe h3{font-weight:400;font-size:15px;color:#555;text-align:center;margin-top:16px}
.more-link{font-size:14px;color:var(--purple)}

/* articles */
.article{left:88px;width:1024px;height:214px;background:var(--card);box-shadow:0 4px 18px rgba(0,0,0,.09);display:flex}
.article .thumb{width:352px;height:100%;flex:none}
.article .body{padding:30px 40px 0;flex:1;position:relative}
.article h3{font-size:15px;font-weight:600;letter-spacing:.5px;text-transform:uppercase}
.article p{font-size:15px;line-height:1.6;color:#666;margin-top:14px;max-width:600px}
.article .meta{position:absolute;left:40px;right:40px;bottom:26px;display:flex;justify-content:space-between;font-size:11px;color:#999;border-top:1px solid var(--line);padding-top:10px}

/* book */
.blob{border-radius:50%;background:var(--lavender)}
.book-cover{left:88px;top:2560px;width:344px;height:520px;background:linear-gradient(160deg,#e43d2a 0%,#d02a1f 55%,#a81d17 100%);box-shadow:0 10px 22px rgba(0,0,0,.2)}
.book-copy{left:464px;top:2568px;width:660px}
.book-copy p{font-size:15px;line-height:1.6;color:#555;margin-bottom:14px}
.features{list-style:none;margin-top:6px}
.features li{display:flex;align-items:center;gap:16px;font-size:15px;color:#444;height:38px}
.btn{display:inline-block;font-size:15px;padding:10px 28px;border-radius:24px}
.btn-primary{background:var(--purple);color:#fff}
.btn-ghost{border:1px solid #b7b1d4;color:var(--purple);background:#fff}
.guarantee{left:680px;top:2976px;width:200px;display:flex;gap:12px;align-items:center;font-size:10px;color:#888;line-height:1.4}
.badge{width:52px;height:52px;border-radius:50%;background:#c8a13a;flex:none}
.book-mockup{left:804px;top:2720px;width:308px;height:236px;background:linear-gradient(170deg,#f4d24a 0%,#d53a28 55%,#8d1f19 100%);border-radius:4px}

/* reviews */
.reviews-head{top:3232px;left:0;width:1200px;text-align:center}
.reviews-head h2{font-size:20px;font-weight:500;color:#444}
.stars{display:flex;justify-content:center;gap:4px;margin-top:10px}
.review-card{left:88px;top:3328px;width:1032px;height:330px;background:#fff;box-shadow:0 4px 22px rgba(0,0,0,.09);padding:40px 48px;display:grid;grid-template-columns:1fr 1fr;column-gap:60px}
.reviewer{display:flex;gap:14px;align-items:center}
.avatar{width:44px;height:44px;border-radius:50%;background:linear-gradient(135deg,#c9b49a,#8c7560)}
.reviewer strong{font-size:15px;font-weight:500;display:block}
.reviewer small{font-size:10px;color:#999}
.review-card .mini-stars{display:flex;gap:2px;margin:3px 0}
.review-card p{font-size:14px;line-height:1.6;color:#666;margin-top:20px}

/* faq */
.faq{left:88px;top:3868px;width:1032px;display:grid;grid-template-columns:1fr 1fr;column-gap:48px;row-gap:16px}
.faq-item{height:52px;border:1px solid var(--line);border-radius:4px;display:flex;align-items:center;justify-content:space-between;padding:0 20px;font-size:15px;color:#444;background:#fff}
.faq-note{left:0;top:4100px;width:1200px;text-align:center;font-size:15px;color:#555}
.faq-note a{color:var(--orange);text-decoration:none}

/* signup */
.signup{left:88px;top:4232px;width:1032px;height:440px;background:#fff;box-shadow:0 4px 22px rgba(0,0,0,.08);display:flex}
.signup .thumb{width:424px;height:100%;flex:none;background:linear-gradient(170deg,#f4f1ea 0%,#f28b6b 45%,#e04a3e 75%,#f7e1d4 100%)}
.signup-form{padding:44px 56px}
.signup-form h2{font-family:"Poppins",sans-serif;font-weight:500;font-size:22px;line-height:1.45;color:#222}
.field{width:440px;height:48px;background:#f3f3f3;border-radius:4px;margin-top:16px;font-size:14px;color:#999;display:flex;align-items:center;padding:0 18px}
.signup-form .btn{margin-top:20px}
.consent{font-size:10px;color:#999;margin-top:12px;line-height:1.5}
.consent u{color:var(--purple)}

/* footer */
.site-footer{left:0;top:4800px;width:1200px;height:56px;background:var(--footer);display:flex;justify-content:center;align-items:center;gap:36px;color:#fff;font-size:14px}
</style>
</head>
<body>
<div class="page">

  <header class="site-header abs">
    <div class="brand">Nectar Notes</div>
    <div class="tagline">The healing power of natural juicing &amp; smoothie recipes</div>
    <nav class="main-nav"><span>Home</span><span>Articles</span><span>Contact</span><span>About</span><span>Recipes</span><span>Affiliates</span></nav>
  </header>

  <section class="hero abs">
    <div class="hero-img" role="img" aria-label="Row of glass jars filled with colourful fresh juices and straws"></div>
    <div class="slider-arrow abs" style="left:4px"><svg width="16" height="26"><path d="M13 2 3 13l10 11" fill="none" stroke="#fff" stroke-width="3"/></svg></div>
    <div class="slider-arrow abs" style="right:4px"><svg width="16" height="26"><path d="M3 2l10 11L3 24" fill="none" stroke="#fff" stroke-width="3"/></svg></div>
    <div class="slider-dots abs"><span class="on"></span><span></span><span></span></div>
  </section>
  <div class="hero-strip abs">
    <p>Deliver more nutrients to your body than you could ever get from even the best supplements.</p>
    <p>Recipes that heal! eBook available for immediate download. Get over 275 delicious recipes.</p>
    <p>Fight specific illnesses based on actual nutritional research, not hearsay.</p>
  </div>

  <div class="pill abs" style="left:88px;top:792px">Juice and smoothie recipes</div>

  <article class="recipe abs" style="left:88px;top:860px"><div class="thumb" role="img" aria-label="Strawberry acai smoothie glasses" style="background:linear-gradient(160deg,#e9e4e0,#c7333a 55%,#7a1d22)"></div><h3>Strawberry Acai Smoothie</h3></article>
  <article class="recipe abs" style="left:444px;top:860px"><div class="thumb" role="img" aria-label="Green smoothie in a glass" style="background:linear-gradient(160deg,#e7ece2,#7fae4a 55%,#3e6a2a)"></div><h3>Post Workout Green Smoothie</h3></article>
  <article class="recipe abs" style="left:808px;top:860px"><div class="thumb" role="img" aria-label="Orange peach punch glasses" style="background:linear-gradient(160deg,#f1e9e2,#f08a3a 55%,#c8401f)"></div><h3>Orange Peach Punch</h3></article>
  <article class="recipe abs" style="left:88px;top:1180px"><div class="thumb" role="img" aria-label="Dark berry smoothie in a jar" style="background:linear-gradient(160deg,#4c3a44,#86293b 55%,#2e2226)"></div><h3>Post Workout Green Smoothie</h3></article>
  <article class="recipe abs" style="left:444px;top:1180px"><div class="thumb" role="img" aria-label="Pale peach smoothie in a tall glass" style="background:linear-gradient(160deg,#efe8e6,#e9c6c0 55%,#c79d95)"></div><h3>Orange Peach Punch</h3></article>
  <article class="recipe abs" style="left:808px;top:1180px"><div class="thumb" role="img" aria-label="Purple berry smoothies with fruit" style="background:linear-gradient(160deg,#efe6ee,#a25aa0 55%,#5e2c6a)"></div><h3>Strawberry Acai Smoothie</h3></article>
  <div class="more-link abs" style="left:88px;top:1490px">View all recipes ›</div>

  <div class="pill abs" style="left:88px;top:1588px">Must-read articles</div>

  <article class="article abs" style="top:1652px">
    <div class="thumb" role="img" aria-label="Wheatgrass growing in clay pots" style="background:linear-gradient(170deg,#e6e2dc,#8db24a 45%,#a65a34 80%)"></div>
    <div class="body"><h3>Grow your own wheatgrass</h3><p>Wheatgrass is a food made from the Triticum aestivum plant. It's regarded as a super potent health food with amazing benefits...</p><div class="meta"><span>Continue reading ›</span><span>5 min read</span></div></div>
  </article>
  <article class="article abs" style="top:1912px">
    <div class="thumb" role="img" aria-label="Fruit and vegetables on a dark table" style="background:linear-gradient(170deg,#3a3a3c,#6f6a62 50%,#2a2a2c)"></div>
    <div class="body"><h3>How to avoid the dangers</h3><p>Wheatgrass is a food made from the Triticum aestivum plant. It's regarded as a super potent health food with amazing benefits...</p><div class="meta"><span>Continue reading ›</span><span>4 min read</span></div></div>
  </article>
  <article class="article abs" style="top:2172px">
    <div class="thumb" role="img" aria-label="Fresh lettuce growing in a backyard garden" style="background:linear-gradient(170deg,#b7dc6c,#6fa83a 50%,#3f7a26)"></div>
    <div class="body"><h3>Greens in your own backyard</h3><p>Wheatgrass is a food made from the Triticum aestivum plant. It's regarded as a super potent health food with amazing benefits...</p><div class="meta"><span>Continue reading ›</span><span>6 min read</span></div></div>
  </article>
  <div class="more-link abs" style="left:88px;top:2420px">View all articles ›</div>

  <div class="blob abs" style="left:-180px;top:2480px;width:700px;height:700px"></div>
  <div class="book-cover abs" role="img" aria-label="Cover of the ebook Nectar &amp; Blend Formulas For Vigor by Dorian Vellacott"></div>
  <div class="book-copy abs">
    <p>Discover the healing power of fresh juice and smoothies with recipes proven to help prevent and even treat diseases based on the latest scientific research.</p>
    <p>This ebook is packed with recipes based on the latest scientific research AND ancient traditional medicine. Many of our modern medicines were discovered by studying folk remedies: willow bark (pain relief) and valerian root (calming aid) are just 2 examples.</p>
    <ul class="features">
      <li><svg width="20" height="20"><path d="M10 2l2.4 5 5.4.6-4 3.7 1.1 5.4L10 14l-4.9 2.7 1.1-5.4-4-3.7 5.4-.6z" fill="none" stroke="#666" stroke-width="1.4"/></svg>From the "Juicing Expert" for Vitalwire</li>
      <li><svg width="20" height="20"><rect x="3" y="2" width="14" height="16" rx="2" fill="none" stroke="#666" stroke-width="1.4"/><path d="M7 10l2 2 4-4" fill="none" stroke="#666" stroke-width="1.4"/></svg>Doctor recommended</li>
      <li><svg width="20" height="20"><rect x="3" y="3" width="14" height="14" rx="2" fill="none" stroke="#666" stroke-width="1.4"/><path d="M6 6l8 8" stroke="#666" stroke-width="1.4"/></svg>No added sweeteners</li>
      <li><svg width="20" height="20"><circle cx="10" cy="10" r="7.5" fill="none" stroke="#666" stroke-width="1.4"/><path d="M10 6v8M7.5 8h4a1.5 1.5 0 010 3h-3a1.5 1.5 0 000 3h4" fill="none" stroke="#666" stroke-width="1.2"/></svg>Same incredibly low price</li>
    </ul>
  </div>
  <div class="book-mockup abs" role="img" aria-label="Printed hardcopy books stacked in 3D"></div>
  <div class="abs" style="left:464px;top:2976px"><span class="btn btn-primary">Get the eBook</span></div>
  <div class="abs" style="left:464px;top:3038px"><span class="btn btn-ghost">Learn more</span></div>
  <div class="guarantee abs"><div class="badge"></div><span>Protected by 30-day risk-free<br>money-back guarantee</span></div>

  <div class="blob abs" style="left:900px;top:3300px;width:520px;height:520px"></div>
  <div class="reviews-head abs">
    <h2>Reviews from over 30,000 customers</h2>
    <div class="stars">
      <svg width="22" height="22"><path d="M11 1l3 6.5 7 .8-5.2 4.8 1.4 7L11 16.6 4.8 20l1.4-7L1 8.3l7-.8z" fill="var(--star)"/></svg>
      <svg width="22" height="22"><path d="M11 1l3 6.5 7 .8-5.2 4.8 1.4 7L11 16.6 4.8 20l1.4-7L1 8.3l7-.8z" fill="var(--star)"/></svg>
      <svg width="22" height="22"><path d="M11 1l3 6.5 7 .8-5.2 4.8 1.4 7L11 16.6 4.8 20l1.4-7L1 8.3l7-.8z" fill="var(--star)"/></svg>
      <svg width="22" height="22"><path d="M11 1l3 6.5 7 .8-5.2 4.8 1.4 7L11 16.6 4.8 20l1.4-7L1 8.3l7-.8z" fill="var(--star)"/></svg>
      <svg width="22" height="22"><path d="M11 1l3 6.5 7 .8-5.2 4.8 1.4 7L11 16.6 4.8 20l1.4-7L1 8.3l7-.8z" fill="var(--star)"/></svg>
    </div>
  </div>
  <section class="review-card abs">
    <div>
      <div class="reviewer"><div class="avatar" role="img" aria-label="Reviewer avatar"></div><div><strong>Marlo K.</strong><div class="mini-stars"><svg width="60" height="11"><g fill="var(--star)"><circle cx="5" cy="5.5" r="4.5"/><circle cx="17" cy="5.5" r="4.5"/><circle cx="29" cy="5.5" r="4.5"/><circle cx="41" cy="5.5" r="4.5"/><circle cx="53" cy="5.5" r="4.5"/></g></svg></div><small>Reviewed on October 2021</small></div></div>
      <p>I had ordered this book and returned it because the book format did not suit me. I suggested to Dorian that the book could be laid better like with an index. Dorian took my and other reviewers suggestions and published the new 5th edition complete with our suggestions.</p>
    </div>
    <div>
      <div class="reviewer"><div class="avatar" role="img" aria-label="Reviewer avatar"></div><div><strong>Tessa R.</strong><div class="mini-stars"><svg width="60" height="11"><g fill="var(--star)"><circle cx="5" cy="5.5" r="4.5"/><circle cx="17" cy="5.5" r="4.5"/><circle cx="29" cy="5.5" r="4.5"/><circle cx="41" cy="5.5" r="4.5"/><circle cx="53" cy="5.5" r="4.5"/></g></svg></div><small>Reviewed on September 2021</small></div></div>
      <p>I am a big fan of 'Nectar Notes with Dorian' on social media and I have learned a ton of valuable juicing tips that have helped me along the way. This book is a concise, well researched collection of some of his very best with wonderful recipes to explore. Good stuff. Thanks Dorian!</p>
    </div>
  </section>
  <div class="more-link abs" style="left:136px;top:3612px">See all reviews ›</div>

  <div class="pill abs" style="left:444px;top:3800px;text-transform:none;font-size:18px;font-weight:500;padding:9px 34px">Frequently Asked Questions</div>
  <section class="faq abs">
    <div class="faq-item">How many days should I do a cleanse for?<svg width="14" height="9"><path d="M1 1l6 6 6-6" fill="none" stroke="#777" stroke-width="1.6"/></svg></div>
    <div class="faq-item">How many days should I do a cleanse for?<svg width="14" height="9"><path d="M1 1l6 6 6-6" fill="none" stroke="#777" stroke-width="1.6"/></svg></div>
    <div class="faq-item">Do you add water to your juices?<svg width="14" height="9"><path d="M1 1l6 6 6-6" fill="none" stroke="#777" stroke-width="1.6"/></svg></div>
    <div class="faq-item">Do you add water to your juices?<svg width="14" height="9"><path d="M1 1l6 6 6-6" fill="none" stroke="#777" stroke-width="1.6"/></svg></div>
    <div class="faq-item">Can I order Online and pick up in-store?<svg width="14" height="9"><path d="M1 1l6 6 6-6" fill="none" stroke="#777" stroke-width="1.6"/></svg></div>
    <div class="faq-item">Can I order Online and pick up in-store?<svg width="14" height="9"><path d="M1 1l6 6 6-6" fill="none" stroke="#777" stroke-width="1.6"/></svg></div>
  </section>
  <p class="faq-note abs">Got more questions? <a>Send us an email</a> instead</p>

  <section class="signup abs">
    <div class="thumb" role="img" aria-label="Glasses of strawberry lemonade with fresh fruit"></div>
    <div class="signup-form">
      <h2>Sign Up to Get the Best &amp; Latest Tips &amp; Tricks<br>for the Most Delicious &amp; Nutritious Fresh Juice</h2>
      <div class="field">Name</div>
      <div class="field">Email address</div>
      <span class="btn btn-primary">Sign Me Up</span>
      <p class="consent">By signing up, you agree to our <u>Terms and Conditions</u><br>and <u>Privacy Policy</u>.</p>
    </div>
  </section>

  <footer class="site-footer abs"><span>Articles</span><span>Contact</span><span>About</span><span>Recipes</span><span>Affiliates</span><span>Nectar Notes / 2021</span></footer>
</div>
</body>
</html>
```